Business Card for Lorena Whitfield

Name: Lorena Whitfield
Title: Realtor
Email: Lorena@LorenaWhitfieldRE.com
Phone: 480-555-0137

On the front of the business card, I would like the photo, the contact information and the Lorena Whitfield Logo. The backside is required to have the Broker logo and the required logos. Please use the colors from the logo design. Our company has a classy, professional look.

```html
<!DOCTYPE html>
<html lang="en">
<head>
<meta charset="utf-8">
<title>Lorena Whitfield Business Card</title>
<link href="https://fonts.googleapis.com/css2?family=Cinzel:wght@400;600&family=EB+Garamond:wght@400&display=swap" rel="stylesheet">
<style>
  :root {
    --backdrop: #d4d4d4;
    --card: #ffffff;
    --brand-red: #c8202f;
    --ink-gray: #4a4a4a;
    --rule-gray: #6b6b6b;
    --ink-black: #1b1b1b;
    --photo-light: #e9e9e9;
    --photo-dark: #3a3a3a;
  }
  * { margin: 0; padding: 0; box-sizing: border-box; }
  html, body {
    width: 1200px; height: 800px; overflow: hidden;
    background: var(--backdrop);
  }
  .sheet {
    position: relative; width: 1200px; height: 800px;
    display: flex; align-items: center; justify-content: center; gap: 40px;
  }
  .card {
    position: relative; width: 540px; height: 309px;
    background: var(--card); overflow: hidden;
    box-shadow: 0 6px 18px rgba(0,0,0,0.18);
  }

  /* Front */
  .front-logo {
    position: absolute; left: 150px; top: 34px;
    display: flex; align-items: center; gap: 12px;
  }
  .front-logo__mark {
    width: 44px; height: 44px; background: var(--brand-red);
  }
  .front-logo__text { display: flex; flex-direction: column; }
  .front-logo__name {
    font-family: "Cinzel", serif; font-weight: 600; font-size: 25px;
    color: var(--brand-red); letter-spacing: 1px; line-height: 1;
    padding-bottom: 5px; border-bottom: 1.5px solid var(--rule-gray);
  }
  .front-logo__sub {
    font-family: "Cinzel", serif; font-size: 10px; color: var(--ink-gray);
    letter-spacing: 1.5px; text-align: right; margin-top: 3px;
  }
  .agent {
    position: absolute; left: 30px; top: 120px; width: 260px;
    font-family: "EB Garamond", serif; color: var(--ink-gray);
  }
  .agent__name {
    font-family: "Cinzel", serif; font-size: 17px; letter-spacing: 1px; line-height: 1.1;
  }
  .agent__title {
    font-family: "Cinzel", serif; font-size: 12px; letter-spacing: 1px;
    padding-bottom: 6px; border-bottom: 1px solid var(--rule-gray);
  }
  .agent__contact { list-style: none; margin-top: 6px; font-size: 13px; line-height: 1.5; }
  .agent__contact li { display: flex; align-items: center; gap: 6px; }
  .agent__contact svg { width: 11px; height: 11px; flex: none; }
  .portrait {
    position: absolute; right: 60px; bottom: 0; width: 210px; height: 200px;
    background: radial-gradient(ellipse at 55% 30%, var(--photo-light) 0 18%, #9a9a9a 30%, var(--photo-dark) 60%);
    border-radius: 90px 90px 0 0;
  }

  /* Back */
  .broker {
    position: absolute; left: 0; right: 0; top: 108px;
    display: flex; flex-direction: column; align-items: center; gap: 8px;
  }
  .broker__mark { width: 46px; height: 46px; border-radius: 50%; background: var(--ink-black); }
  .broker__name {
    font-family: "Cinzel", serif; font-size: 20px; letter-spacing: 3px; color: var(--ink-black);
  }
  .broker__sub {
    font-family: "Cinzel", serif; font-size: 9px; letter-spacing: 2px; color: var(--ink-black); margin-top: -6px;
  }
  .badges {
    position: absolute; right: 40px; bottom: 30px; display: flex; gap: 6px; align-items: flex-end;
  }
  .badge { border: 1.5px solid var(--ink-black); background: var(--card); }
  .badge--housing { width: 30px; height: 30px; }
  .badge--member { width: 26px; height: 32px; }
  .badge--listing { width: 48px; height: 24px; }
</style>
</head>
<body>
<main class="sheet">
  <section class="card card--front">
    <div class="front-logo">
      <div class="front-logo__mark"></div>
      <div class="front-logo__text">
        <span class="front-logo__name">LORENA WHITFIELD</span>
        <span class="front-logo__sub">REAL ESTATE</span>
      </div>
    </div>
    <div class="agent">
      <p class="agent__name">LORENA WHITFIELD</p>
      <p class="agent__title">REALTOR</p>
      <ul class="agent__contact">
        <li>
          <svg viewBox="0 0 12 12"><path d="M3 1 L5 3.5 L4 5 Q5 7 7 8 L8.5 7 L11 9 L9.5 11 Q4 10.5 1 3 Z" fill="#c8202f"/></svg>
          480-555-0137
        </li>
        <li>
          <svg viewBox="0 0 12 12"><rect x="0.5" y="2" width="11" height="8" fill="#c8202f"/><path d="M0.5 2 L6 6.5 L11.5 2" stroke="#fff" fill="none"/></svg>
          Lorena@LorenaWhitfieldRE.com
        </li>
      </ul>
    </div>
    <div class="portrait" role="img" aria-label="Black and white portrait of the agent in a dark sweater"></div>
  </section>

  <section class="card card--back">
    <div class="broker">
      <div class="broker__mark"></div>
      <span class="broker__name">ASHBURY CREST</span>
      <span class="broker__sub">REAL ESTATE</span>
    </div>
    <div class="badges">
      <div class="badge badge--housing"></div>
      <div class="badge badge--member"></div>
      <div class="badge badge--listing"></div>
    </div>
  </section>
</main>
</body>
</html>
```